Schnapsbrennerei sucht neue Etiketten
Zielgruppe
Wir sind eine örtliche Schnapsbrennerei, die inzwischen seit ein paar Jahren einen eigenen Kundenstamm aufgebaut hat. Nun werden wir im nächsten Jahr einen neuen Verkaufsraum bauen. Aus diesem Grund wollen wir unsere Etiketten komplett überarbeiten.
Ein neues Logo habe ich bereits designen lassen. Diese finden Sie unten im Dokumententenupload. Wir legen viel Wert auf eine sehr hohe Qualität, welche sich sowohl in unserem Logo als auch den Etiketten Wiederspiegeln soll.
Unsere Kundschaft ist hauptsächlich Ü35 und legt viel Wert auf hochwertige Produkte.
Aufgabenstellung
Eines direkt vorne weg: Da wir unsere komplette Produktpalette neu gestalten wollen würde ich Sie bitten, der Einfachheit halber zuerst nur ein Schnapsetikett (z.B. Zwetschge oder Willi), ein Likör Etikett und ein Etikett für unseren Whiskey zu erstellen.
Darüber hinaus bitte ich Sie auch ein Design für unseren neuen Gin und einen Aquavit, welcher im Herbst auf den Markt kommen soll zu designen. Im Anschluss daran, werde ich in der Zusammenarbeit mit Ihnen die Etiketten optimieren wollen.
Sobald ein 'Grundetikett' entstanden ist, sollen dann auch die anderen Schnäpse und Liköre in dem gleichen Stil erstellt werden. Explizit möchte ich daraufhin weisen, dass sowohl die Whiskeys als auch der Gin und der Aquavit nicht zwangsläufig das gleiche 'Grundetikett' wie der Schnaps und der Likör haben sollen. Ist bei unseren aktuellen Etiketten auch nicht der Fall. Sehen Sie in den Bildern unten.
Wir verkaufen unseren Schnaps und Likör in 3 unterschieldichen Größen 0,2; 0,5 und 1,0 Liter. Wir verwenden für die 0,2 und 0,5 die Flasche Tessa. Das Etikett der 0,5er Flasche soll in etwa 65x120-130 mm sein. Hier sind wir allerdings variabel.
Dieses entstandene Etikett soll dann auf die anderen Flaschen entsprechend angepasst werden.
Sie finden im Dokumentenupload unsere aktuellen Etiketten und das Logo, welches eingebaut werden soll. Auch ein Etikett von einem örtlichen Weingut, welches mir vom Aufbau und der Unterteilung sehr gut gefällt, werde ich mit anhängen. Allerdings ist dieses Bild sehr unscharf. Wie gesagt es geht hierbei hauptsächlich um die Einteilung mit den oberen und den unteren 'Rahmen'.
Auch unsere Preisliste finden Sie Anhang, wobei diese noch in der Rohform ist und das Obst so nicht verwendet wird, aber hier sind die meisten Produkte drauf.
Das Logo gibt es in verschiedenen Farben. Gerne dürfen Sie für die unterschiedlichen Produkte auch unterschiedliche Farben nutzen.
Was ich mir persönlich g..

```html
<!DOCTYPE html>
<html lang="de">
<head>
<meta charset="utf-8">
<title>Hollweger's Whiskey – Etikett</title>
<link rel="stylesheet" href="https://fonts.googleapis.com/css2?family=Oranienbaum&family=Oswald:wght@500&family=Montserrat:wght@500&family=Poppins:wght@600&display=swap">
<style>
  :root {
    --backdrop: #d9d9d9;
    --cream: #f3f0e8;
    --wine: #6d1f1f;
    --wine-text: #6a1a1a;
    --gold: #c4a03c;
    --gold-line: #c9a74a;
    --white: #ffffff;
  }
  * { margin: 0; padding: 0; box-sizing: border-box; }
  html, body { width: 1200px; height: 960px; overflow: hidden; }
  body { background: var(--backdrop); position: relative; }

  .label {
    position: absolute; left: 260px; top: 90px;
    width: 680px; height: 780px;
    background: var(--cream);
    overflow: hidden;
  }
  .label__frame {
    position: absolute; left: 14px; right: 14px; top: 26px; bottom: 40px;
    border: 2px solid var(--gold-line);
  }
  .label__tab {
    position: absolute; left: 256px; top: 0; width: 169px; height: 247px;
    background: var(--wine);
  }
  .label__tab-frame {
    position: absolute; left: 18px; right: 18px; top: 0; bottom: 18px;
    border: 2px solid var(--gold-line); border-top: none;
  }
  .brand-mark {
    position: absolute; left: 0; right: 0; top: 92px;
    display: flex; flex-direction: column; align-items: center; gap: 10px;
    color: var(--cream);
    font-family: "Oswald", sans-serif; font-weight: 500;
    font-size: 17px; letter-spacing: 2px;
  }
  .brand-mark__dot {
    width: 26px; height: 26px; border-radius: 50%;
    background: var(--cream);
  }
  .product-name {
    position: absolute; left: 0; right: 0; top: 278px;
    text-align: center; color: var(--gold);
    font-family: "Oranienbaum", serif;
    font-size: 112px; line-height: 1; letter-spacing: 3px;
  }
  .product-type {
    position: absolute; left: 0; right: 0; top: 410px;
    text-align: center; color: var(--gold);
    font-family: "Oranienbaum", serif;
    font-size: 86px; line-height: 1; letter-spacing: 3px;
  }
  .product-note {
    position: absolute; left: 0; right: 0; top: 518px;
    text-align: center; color: var(--wine-text);
    font-family: "Oswald", sans-serif; font-weight: 500;
    font-size: 27px; line-height: 33px; text-transform: uppercase;
  }
  .product-abv {
    position: absolute; left: 30px; top: 513px;
    color: var(--wine-text); font-family: "Poppins", sans-serif; font-weight: 600;
  }
  .product-abv__value { display: block; font-size: 26px; letter-spacing: 1px; }
  .product-abv__kind { display: block; font-size: 19px; }
  .product-volume {
    position: absolute; right: 36px; top: 513px;
    color: var(--wine-text); font-family: "Poppins", sans-serif; font-weight: 600;
    font-size: 26px; letter-spacing: 1px;
  }
  .label__band {
    position: absolute; left: 0; right: 0; top: 594px; bottom: 0;
    background: var(--wine);
  }
  .label__band-line {
    position: absolute; left: 14px; right: 14px; top: 150px;
    border-top: 2px solid var(--gold-line);
  }
  .producer {
    position: absolute; left: 0; right: 0; top: 52px;
    text-align: center; color: var(--white);
    font-family: "Montserrat", sans-serif; font-weight: 500;
    font-size: 19px; line-height: 28px; text-transform: uppercase;
  }
</style>
</head>
<body>
  <section class="label">
    <div class="label__frame"></div>
    <div class="label__band">
      <div class="label__band-line"></div>
      <p class="producer">Edelbrände &amp; Liköre Edmund Hollweger<br>Lindenstraße 12 - D97421 Musterdorf - Telefon 0 90 12 - 4580</p>
    </div>
    <div class="label__tab">
      <div class="label__tab-frame"></div>
      <div class="brand-mark">
        <span class="brand-mark__dot"></span>
        <span>HOLLWEGER</span>
      </div>
    </div>
    <h1 class="product-name">HOLLWEGER’S</h1>
    <h2 class="product-type">WHISKEY</h2>
    <p class="product-abv"><span class="product-abv__value">40% vol.</span><span class="product-abv__kind">Spirituose</span></p>
    <p class="product-note">Im Holzfass gereift<br>Special Edition</p>
    <p class="product-volume">0,5 l</p>
  </section>
</body>
</html>
```